Require a Business card , letter head and envelope for my company named Swift Amber,

Swift Amber is a trading company dealing with multiple products in the following categories. Home , kitchen, furniture, Grocery, health. fitness etc.
I am attaching the logo designed by gigvault .in.
The business card should include the Following
1)name :Manoj T S
2)Designation : VP Product Innovation
3)Mobile no +91 9456017734
4)Emailid :manoj@swiftamber .com
5)Web site: swiftamber.com
6) Company Logo
7) Company address( can be on the reverse side also): Swift Amber, 41/562C, LMVS Road, Kovilpadi, Varunagar 673049, Sahyadri , India
The letter head and envelope, should include the following ,
Logo , Email id , Web site address ,and the postal address.

```html
<!DOCTYPE html>
<html lang="en">
<head>
<meta charset="utf-8">
<title>Swift Amber – Business Card</title>
<link rel="stylesheet" href="https://fonts.googleapis.com/css2?family=Questrial&family=Montserrat:wght@600&display=swap">
<style>
  :root {
    --stage: #3a3a3a;
    --card-light: #f4f4f4;
    --card-mid: #b9b9b9;
    --card-dark: #8a8a8a;
    --disc: rgba(255,255,255,0.18);
    --disc-dark: rgba(0,0,0,0.10);
    --accent: #e2161d;
    --ink: #2a2a2a;
    --ink-soft: #f2f2f2;
  }
  * { margin: 0; padding: 0; box-sizing: border-box; }
  html, body { width: 1200px; height: 1200px; overflow: hidden; }
  body {
    background: var(--stage);
    font-family: "Questrial", "Century Gothic", sans-serif;
    position: relative;
  }
  .card {
    position: absolute;
    left: 180px;
    width: 840px;
    height: 480px;
    overflow: hidden;
    box-shadow: 0 14px 30px rgba(0,0,0,0.45);
  }
  .card--brand {
    top: 80px;
    background: radial-gradient(ellipse at 50% 45%, var(--card-light) 0%, var(--card-mid) 55%, var(--card-dark) 100%);
  }
  .card--contact {
    top: 640px;
    background: radial-gradient(ellipse at 40% 45%, #d6d6d6 0%, #9c9c9c 55%, #6f6f6f 100%);
  }
  .disc {
    position: absolute;
    border-radius: 50%;
    background: var(--disc);
  }
  .card--brand .disc--top-left { width: 300px; height: 300px; left: -120px; top: -110px; }
  .card--brand .disc--bottom-right { width: 260px; height: 260px; right: -110px; bottom: -120px; }
  .card--contact .disc--left { width: 280px; height: 280px; left: -140px; top: 150px; background: var(--disc-dark); }
  .card--contact .disc--right { width: 300px; height: 300px; right: -150px; top: -70px; background: var(--disc-dark); }

  .brand {
    position: absolute;
    left: 0; right: 0; top: 130px;
    display: flex; flex-direction: column; align-items: center; gap: 30px;
  }
  .brand__mark {
    width: 140px; height: 140px; border-radius: 50%;
    background: var(--accent);
  }
  .brand__name {
    font-family: "Montserrat", sans-serif;
    font-weight: 600;
    font-size: 46px;
    letter-spacing: 1px;
    color: var(--accent);
  }

  .rule { position: absolute; background: var(--accent); }
  .rule--top-left { left: 0; top: 0; width: 140px; height: 9px; }
  .rule--top-right { right: 0; top: 0; width: 370px; height: 7px; }
  .rule--bottom-left { left: 0; bottom: 0; width: 170px; height: 8px; }
  .rule--bottom-right { right: 0; bottom: 0; width: 420px; height: 8px; }

  .person__name {
    position: absolute; left: 40px; top: 18px;
    font-size: 132px; line-height: 1; font-weight: 400;
    color: var(--accent);
    text-shadow: 1px 1px 0 #5a0a0c, 0 3px 6px rgba(0,0,0,0.3);
  }
  .person__title {
    position: absolute; left: 235px; top: 182px;
    font-size: 34px; letter-spacing: 3px;
    color: var(--ink-soft);
  }
  .contact-list {
    position: absolute; left: 36px; top: 290px;
    list-style: none;
    font-size: 24px; color: var(--ink-soft);
    display: flex; flex-direction: column; gap: 12px;
  }
  .contact-list li { display: flex; align-items: center; gap: 12px; }
  .contact-list svg { width: 22px; height: 22px; flex: none; }
  .address {
    position: absolute; right: 90px; top: 280px;
    font-style: normal; text-align: right;
    font-size: 24px; line-height: 1.45;
    color: var(--ink);
  }
  .address__pin { position: absolute; right: 30px; top: 372px; width: 40px; height: 54px; }
</style>
</head>
<body>
  <section class="card card--brand" aria-label="Card back with company name">
    <span class="disc disc--top-left"></span>
    <span class="disc disc--bottom-right"></span>
    <div class="brand">
      <span class="brand__mark"></span>
      <span class="brand__name">SWIFT AMBER</span>
    </div>
  </section>

  <section class="card card--contact" aria-label="Card front with contact details">
    <span class="disc disc--left"></span>
    <span class="disc disc--right"></span>
    <span class="rule rule--top-left"></span>
    <span class="rule rule--top-right"></span>
    <span class="rule rule--bottom-left"></span>
    <span class="rule rule--bottom-right"></span>

    <h1 class="person__name">Manoj ts</h1>
    <p class="person__title">VP Product Innovation</p>

    <ul class="contact-list">
      <li>
        <svg viewBox="0 0 24 24"><path fill="#e2161d" d="M6.6 10.8a15 15 0 0 0 6.6 6.6l2.2-2.2a1 1 0 0 1 1-.25 11.4 11.4 0 0 0 3.6.57 1 1 0 0 1 1 1V20a1 1 0 0 1-1 1A17 17 0 0 1 3 4a1 1 0 0 1 1-1h3.5a1 1 0 0 1 1 1c0 1.25.2 2.450.57 3.57a1 1 0 0 1-.25 1z"/></svg>
        +91 9456017734
      </li>
      <li>
        <svg viewBox="0 0 24 24"><rect x="2" y="5" width="20" height="14" rx="2" fill="none" stroke="#e2161d" stroke-width="2"/><path d="M3 6l9 7 9-7" fill="none" stroke="#e2161d" stroke-width="2"/></svg>
        manoj@swiftamber .com
      </li>
      <li>
        <svg viewBox="0 0 24 24"><circle cx="12" cy="12" r="9" fill="none" stroke="#e2161d" stroke-width="2"/><path d="M3 12h18M12 3c3 3 3 15 0 18M12 3c-3 3-3 15 0 18" fill="none" stroke="#e2161d" stroke-width="1.6"/></svg>
        swiftamber.com
      </li>
    </ul>

    <address class="address">
      Swift Amber, 41/562C,<br>
      LMVS Road, Kovilpadi,<br>
      Varunagar 673049, Sahyadri , India
    </address>
    <svg class="address__pin" viewBox="0 0 40 54" aria-hidden="true">
      <path fill="#e2161d" d="M20 0C9 0 0 9 0 20c0 14 20 34 20 34s20-20 20-34C40 9 31 0 20 0z"/>
      <circle cx="20" cy="19" r="7" fill="#9c9c9c"/>
    </svg>
  </section>
</body>
</html>
```